Banner Design Project

I need a banner designed that will be used in an outdoor location. The banner is 8' x 3' and can be full color.

This is a general advertising banner for a photography business; I can provide images if needed;

My website is: www.darvomkellphotography.com

It will be used at the following school: http://www.qbtrm.com/

Target Market(s)

All ages but should appeal to High School Students

Industry/Entity Type

Advertising

Requirements
Must have
• Integrate Logo

```html
<!DOCTYPE html>
<html lang="en">
<head>
<meta charset="utf-8">
<title>Darvom Kell Photography – Banner Options</title>
<link rel="stylesheet" href="https://fonts.googleapis.com/css2?family=Source+Sans+3:wght@400;600;700&display=swap">
<style>
  :root {
    --stage-top: #2c3034;
    --stage-bottom: #040404;
    --paper: #ffffff;
    --sky-blue: #5ab4e5;
    --navy: #124a8a;
    --ink-grey: #55585b;
    --ring-light: #7fc0e6;
    --ring-dark: #3b6f8c;
    --grey-band-top: #474c50;
    --grey-band-bottom: #9a9c9e;
    --red-band-top: #9c1228;
    --red-band-mid: #d21f45;
    --red-band-bottom: #b3162f;
    --services-red: #c41c3a;
    --shadow: rgba(20, 20, 20, 0.75);
    --photo-sky: #e9e4de;
    --photo-crowd: #7a5a4a;
  }
  * { box-sizing: border-box; margin: 0; padding: 0; }
  html, body {
    width: 1200px;
    height: 1002px;
    overflow: hidden;
  }
  body {
    background: linear-gradient(180deg, var(--stage-top) 0%, #15181a 45%, var(--stage-bottom) 100%);
    font-family: "Source Sans 3", "Myriad Pro", Arial, sans-serif;
    position: relative;
  }
  .banner {
    position: absolute;
    left: 112px;
    width: 920px;
    height: 344px;
    background: var(--paper);
    overflow: hidden;
  }
  .banner--grey { top: 128px; }
  .banner--red { top: 510px; }
  .banner__art {
    position: absolute;
    inset: 0;
    width: 920px;
    height: 344px;
  }
  .banner__title {
    position: absolute;
    left: 370px;
    width: 556px;
    top: 22px;
    text-align: center;
    font-weight: 700;
    font-size: 66px;
    line-height: 1;
    letter-spacing: -0.5px;
    white-space: nowrap;
  }
  .banner__title .first { color: var(--sky-blue); }
  .banner__title .last { color: var(--navy); }
  .banner__subtitle {
    position: absolute;
    left: 370px;
    width: 556px;
    top: 88px;
    text-align: center;
    font-weight: 700;
    font-size: 33px;
    line-height: 1;
    color: var(--ink-grey);
  }
  .banner__services {
    position: absolute;
    left: 370px;
    width: 556px;
    top: 134px;
    text-align: center;
    list-style: none;
    font-size: 18px;
    line-height: 22px;
    color: var(--ink-grey);
    white-space: nowrap;
  }
  .banner--red .banner__services { color: var(--services-red); }
  .brand-mark {
    position: absolute;
    left: 467px;
    top: 253px;
    width: 363px;
    height: 54px;
    display: flex;
    align-items: center;
    justify-content: center;
    gap: 10px;
    background: var(--paper);
  }
  .brand-mark__square {
    flex: none;
    width: 18px;
    height: 18px;
    background: var(--sky-blue);
  }
  .brand-mark__name {
    font-weight: 700;
    font-size: 17px;
    letter-spacing: 1.5px;
    color: var(--navy);
    white-space: nowrap;
  }
  .banner__web {
    position: absolute;
    left: 467px;
    width: 363px;
    top: 312px;
    text-align: center;
    font-size: 14px;
    font-weight: 600;
    color: var(--paper);
    white-space: nowrap;
  }
  .grey-top { stop-color: var(--grey-band-top); }
  .grey-bottom { stop-color: var(--grey-band-bottom); }
  .red-top { stop-color: var(--red-band-top); }
  .red-mid { stop-color: var(--red-band-mid); }
  .red-bottom { stop-color: var(--red-band-bottom); }
  .ring-light { stop-color: var(--ring-light); }
  .ring-dark { stop-color: var(--ring-dark); }
  .sky { stop-color: var(--photo-sky); }
  .crowd { stop-color: var(--photo-crowd); }
  .swoosh { fill: var(--ring-light); }
  .ground-shadow { fill: var(--shadow); }
</style>
</head>
<body>

<section class="banner banner--grey">
  <svg class="banner__art" viewBox="0 0 920 344">
    <defs>
      <linearGradient id="grey-band" x1="0" y1="0" x2="0" y2="1">
        <stop offset="0" class="grey-top"/>
        <stop offset="1" class="grey-bottom"/>
      </linearGradient>
      <linearGradient id="grey-ring" x1="0" y1="0" x2="1" y2="1">
        <stop offset="0" class="ring-dark"/>
        <stop offset="0.6" class="ring-light"/>
        <stop offset="1" class="ring-dark"/>
      </linearGradient>
      <linearGradient id="grey-photo" x1="0" y1="0" x2="0" y2="1">
        <stop offset="0.1" class="sky"/>
        <stop offset="0.55" class="crowd"/>
        <stop offset="1" class="crowd"/>
      </linearGradient>
    </defs>
    <path d="M0,200 C200,190 350,242 463,242 C650,285 830,262 920,176 L920,344 L0,344 Z" fill="url(#grey-band)"/>
    <path class="swoosh" d="M463,240 C640,275 820,245 920,140 L920,178 C830,262 650,285 463,240 Z"/>
    <ellipse class="ground-shadow" cx="245" cy="301" rx="127" ry="20"/>
    <circle cx="166" cy="127" r="200" fill="url(#grey-ring)"/>
    <circle cx="158" cy="111" r="185" fill="url(#grey-photo)" role="img" aria-label="Photo of a wedding party tossing flower petals into the air"/>
  </svg>
  <h1 class="banner__title"><span class="first">DARVOM</span> <span class="last">KELL</span></h1>
  <p class="banner__subtitle">PHOTOGRAPHY</p>
  <ul class="banner__services">
    <li>Portrature / Family / Couples / Wedding / Engagements</li>
    <li>Water/ Surfing / Sports / Action / Events</li>
    <li>Part Photography / Corporate Brochures</li>
    <li>Product Lines</li>
  </ul>
  <div class="brand-mark">
    <span class="brand-mark__square"></span>
    <span class="brand-mark__name">DARVOM KELL PHOTOGRAPHY</span>
  </div>
  <p class="banner__web">www.darvomkellphotography.com</p>
</section>

<section class="banner banner--red">
  <svg class="banner__art" viewBox="0 0 920 344">
    <defs>
      <linearGradient id="red-band" x1="0" y1="0" x2="0" y2="1">
        <stop offset="0" class="red-top"/>
        <stop offset="0.6" class="red-mid"/>
        <stop offset="1" class="red-bottom"/>
      </linearGradient>
      <linearGradient id="red-ring" x1="0" y1="0" x2="1" y2="1">
        <stop offset="0" class="ring-dark"/>
        <stop offset="0.6" class="ring-light"/>
        <stop offset="1" class="ring-dark"/>
      </linearGradient>
      <linearGradient id="red-photo" x1="0" y1="0" x2="0" y2="1">
        <stop offset="0.1" class="sky"/>
        <stop offset="0.55" class="crowd"/>
        <stop offset="1" class="crowd"/>
      </linearGradient>
    </defs>
    <path d="M0,200 C200,190 350,242 463,242 C650,285 830,262 920,176 L920,344 L0,344 Z" fill="url(#red-band)"/>
    <path class="swoosh" d="M463,240 C640,275 820,245 920,140 L920,178 C830,262 650,285 463,240 Z"/>
    <ellipse class="ground-shadow" cx="245" cy="301" rx="127" ry="20"/>
    <circle cx="166" cy="127" r="200" fill="url(#red-ring)"/>
    <circle cx="158" cy="111" r="185" fill="url(#red-photo)" role="img" aria-label="Photo of a wedding party tossing flower petals into the air"/>
  </svg>
  <h1 class="banner__title"><span class="first">DARVOM</span> <span class="last">KELL</span></h1>
  <p class="banner__subtitle">PHOTOGRAPHY</p>
  <ul class="banner__services">
    <li>Portrature / Family / Couples / Wedding / Engagements</li>
    <li>Water/ Surfing / Sports / Action / Events</li>
    <li>Part Photography / Corporate Brochures</li>
    <li>Product Lines</li>
  </ul>
  <div class="brand-mark">
    <span class="brand-mark__square"></span>
    <span class="brand-mark__name">DARVOM KELL PHOTOGRAPHY</span>
  </div>
  <p class="banner__web">www.darvomkellphotography.com</p>
</section>

</body>
</html>
```